Halvorsen Partners Business Card

Halvorsen Partners Civil Construction
Dorian Halvorsen
CEO
555-318-4076
Dorian@HalvorsenCivil.example
www.HalvorsenCivil.example
Site Development
Utility Construction
Excavation
48730 County Route 19
Land O' Lakes, FL 34999

Target Market(s)

Construction and government

Industry/Entity Type

Business

Contact Information for Business Card

I want an unique design that make a statement

Number of Pages Required

1 page

Font styles to use
Other font styles liked:

Colors

Designer to choose colors to be used in the design.

Requirements
Must have
• unique design, feel free to modify or change the color of my logo.
Nice to have
• extra design features like spot UV, foil accents, color edges, unique paper, or any thing that would make my card pop.
• I like the feel of the image that I attached

```html
<!DOCTYPE html>
<html lang="en">
<head>
<meta charset="utf-8">
<title>Halvorsen Partners Business Card</title>
<link rel="stylesheet" href="https://fonts.googleapis.com/css2?family=Cabin:wght@400;500;600&display=swap">
<style>
  :root {
    --stage: #e9eaec;
    --paper: #ffffff;
    --brand-blue: #1f3f8c;
    --brand-blue-soft: #5a74b3;
    --ink-gray: #6b6f75;
    --dark-1: #1a1a1a;
    --dark-2: #5c5e62;
    --white: #ffffff;
  }
  * { box-sizing: border-box; margin: 0; padding: 0; }
  html, body {
    width: 1200px; height: 900px; overflow: hidden;
    background: var(--stage);
    font-family: "Cabin", Arial, sans-serif;
  }
  .canvas { position: relative; width: 1200px; height: 900px; }
  .card {
    position: absolute; width: 620px; height: 354px;
    border-radius: 4px; overflow: hidden;
    box-shadow: 0 10px 28px rgba(0,0,0,.22);
  }

  /* Back of card */
  .card-back {
    left: 110px; top: 70px;
    background: linear-gradient(160deg, var(--dark-2) 0%, #3a3b3e 45%, var(--dark-1) 100%);
  }
  .back-photo {
    position: absolute; inset: 0;
    background: radial-gradient(ellipse at 60% 40%, rgba(200,200,205,.35) 0%, rgba(0,0,0,0) 60%),
                linear-gradient(180deg, rgba(0,0,0,0) 62%, rgba(0,0,0,.9) 100%);
  }
  .back-wordmark {
    position: absolute; left: 36px; top: 120px;
    font-size: 44px; font-weight: 500; line-height: 1.05;
    color: rgba(255,255,255,.16); text-transform: uppercase;
  }
  .service-list {
    position: absolute; right: 70px; top: 44px;
    list-style: none; color: var(--white);
    font-size: 13px; letter-spacing: .5px; text-transform: uppercase;
  }
  .service-list li { display: flex; align-items: center; gap: 10px; margin-bottom: 9px; }
  .service-list li::before {
    content: ""; width: 8px; height: 8px; border-radius: 50%; background: var(--white);
  }

  /* Front of card */
  .card-front { left: 470px; top: 476px; background: var(--paper); }
  .brand {
    position: absolute; left: 34px; top: 92px;
    display: flex; align-items: center; gap: 12px;
  }
  .brand-mark { width: 38px; height: 38px; background: var(--brand-blue); }
  .brand-divider { width: 1px; height: 46px; background: var(--ink-gray); }
  .brand-name {
    font-size: 25px; font-weight: 500; color: var(--brand-blue);
    text-transform: uppercase; line-height: 1;
  }
  .brand-tagline {
    font-size: 13px; color: var(--ink-gray); letter-spacing: 3.5px;
    text-transform: uppercase; margin-top: 4px;
  }
  .machinery-area {
    position: absolute; right: 0; top: 58px; width: 200px; height: 56px;
    background: linear-gradient(90deg, var(--brand-blue-soft) 0%, var(--brand-blue) 100%);
  }
  .address {
    position: absolute; right: 30px; top: 128px;
    text-align: right; font-size: 15px; color: var(--ink-gray); line-height: 1.35;
    font-style: normal;
  }
  .band {
    position: absolute; left: 0; right: 0; top: 196px; height: 14px;
    background: var(--brand-blue);
  }
  .name-bar {
    position: absolute; left: 0; top: 196px; width: 300px; height: 44px;
    background: var(--brand-blue); color: var(--white);
    display: flex; align-items: flex-end; padding: 0 0 8px 34px; gap: 8px;
  }
  .person-name { font-size: 22px; font-weight: 600; }
  .person-role { font-size: 15px; border-left: 1px solid var(--white); padding-left: 8px; }
  .contact-list {
    position: absolute; left: 34px; top: 256px; list-style: none;
    font-size: 16px; color: var(--ink-gray); line-height: 1.45;
  }
  .contact-list li { display: flex; align-items: center; gap: 12px; }
  .contact-list svg { width: 13px; height: 13px; fill: var(--brand-blue); }
</style>
</head>
<body>
<main class="canvas">

  <section class="card card-back" aria-label="Card back">
    <div class="back-photo" role="img" aria-label="Silhouetted excavator and earthmoving trucks against a cloudy grey sky"></div>
    <div class="back-wordmark">Halvorsen<br>Partners</div>
    <ul class="service-list">
      <li>Site Development</li>
      <li>Utility Construction</li>
      <li>Excavation</li>
    </ul>
  </section>

  <section class="card card-front" aria-label="Card front">
    <div class="machinery-area" role="img" aria-label="Blue silhouette of excavator and construction machinery"></div>
    <div class="brand">
      <div class="brand-mark"></div>
      <div class="brand-divider"></div>
      <div>
        <div class="brand-name">Halvorsen Partners</div>
        <div class="brand-tagline">Civil Construction</div>
      </div>
    </div>
    <address class="address">
      48730 County Route 19<br>Land O' Lakes, FL 34999
    </address>
    <div class="band"></div>
    <div class="name-bar">
      <span class="person-name">Dorian Halvorsen</span>
      <span class="person-role">CEO</span>
    </div>
    <ul class="contact-list">
      <li>
        <svg viewBox="0 0 24 24"><path d="M6.6 10.8a15.1 15.1 0 0 0 6.6 6.6l2.2-2.2a1 1 0 0 1 1-.25 11.4 11.4 0 0 0 3.6.57 1 1 0 0 1 1 1V20a1 1 0 0 1-1 1A17 17 0 0 1 3 4a1 1 0 0 1 1-1h3.5a1 1 0 0 1 1 1c0 1.25.2 2.45.57 3.57a1 1 0 0 1-.25 1z"/></svg>
        555-318-4076
      </li>
      <li>
        <svg viewBox="0 0 24 24"><path d="M2 5h20v14H2z M4 7v.5l8 5 8-5V7z" fill-rule="evenodd"/></svg>
        Dorian@HalvorsenCivil.example
      </li>
      <li>
        <svg viewBox="0 0 24 24"><circle cx="12" cy="12" r="10"/></svg>
        www.HalvorsenCivil.example
      </li>
    </ul>
  </section>

</main>
</body>
</html>
```